Shopify store for hemp

I need a store designed for Shopify for my hemp company. I currently have a brick and mortar store, but we are looking to get some business online as well. I will upload our logo for reference. We want a clean look. Categories like THCA Flower, Concentrates, Vapes, Edibles would be nice so that we can put individual products under them. I want something about all products being third-party lab tested. All products are sourced in the United States.
Updates

Target Market(s)

Former customers who live in different areas and signed up for our marketing list.

Industry/Entity Type

Hemp/Cannabis

Coding

Coded - Design and coding required

Number of Pages Required

1 page

Requirements
Must have
• Clean feel

```html
<!DOCTYPE html>
<html lang="en">
<head>
<meta charset="utf-8">
<title>Ridgeline Hemp – Premium Hemp, Lab-Tested for Purity</title>
<link href="https://fonts.googleapis.com/css2?family=Poppins:wght@400;500;600;700&display=swap" rel="stylesheet">
<style>
:root{
  --green:#4a8a45;
  --green-dark:#3d7a39;
  --blue:#1e8fc4;
  --blue-btn:#1f86bd;
  --ink:#1d1d1d;
  --muted:#555;
  --star:#f2b21b;
  --pale:#e3f0f6;
  --white:#fff;
}
*{box-sizing:border-box;margin:0;padding:0}
html,body{width:1200px;height:4673px;overflow:hidden}
body{position:relative;font-family:"Poppins",sans-serif;color:var(--ink);background:var(--white)}
.abs{position:absolute}
.btn{position:absolute;display:flex;align-items:center;justify-content:center;border-radius:22px;color:var(--white);font-size:13px;font-weight:500;letter-spacing:.5px;text-transform:uppercase}
.btn-green{background:var(--green)}
.btn-blue{background:var(--blue-btn)}
.rule{position:absolute;height:4px;width:56px;background:var(--blue);left:572px}
.section-title{position:absolute;left:0;width:1200px;text-align:center;font-size:36px;font-weight:600}
.section-title span{color:var(--green)}

/* hero */
.hero{position:absolute;left:0;top:0;width:1200px;height:640px}
.hero-photo{position:absolute;inset:0;background:radial-gradient(ellipse at 50% 20%,#4b3f7a 0%,#2a2550 35%,#1b2a20 70%,#16301a 100%)}
.hero h1{position:absolute;top:208px;width:1200px;text-align:center;font-size:58px;font-weight:600;line-height:68px;color:var(--white)}
.hero h1 .accent{color:#5da752}
.hero-sub{position:absolute;top:368px;width:1200px;text-align:center;color:var(--white);font-size:14px}
.nav{position:absolute;left:120px;top:44px;width:960px;height:59px;background:var(--white);border-radius:30px;display:flex;align-items:center;font-size:13px}
.nav a{color:var(--ink);text-decoration:none}
.nav .sep{margin:0 14px;color:var(--ink)}
.nav .active{font-weight:600;text-decoration:underline}
.search{position:absolute;left:682px;top:16px;width:166px;height:28px;border-bottom:1px solid var(--ink);font-size:12px;padding-top:4px}
.brand-badge{position:absolute;left:540px;top:6px;width:120px;height:120px;border-radius:50%;background:var(--green);border:5px solid var(--white);display:flex;align-items:center;justify-content:center;text-align:center;color:var(--white);font-size:15px;font-weight:600;line-height:18px}

/* about */
.about-img{position:absolute;border-radius:6px}
.about h2{position:absolute;left:635px;top:716px;font-size:34px;font-weight:600}
.about h2 span{color:var(--green)}
.about p{position:absolute;left:636px;top:806px;width:390px;font-size:13.2px;line-height:24px;text-align:justify;color:#333}

/* categories */
.cat-circle{position:absolute;border-radius:50%;border:4px solid var(--white);overflow:hidden}
.cat-label{position:absolute;left:0;right:0;bottom:22px;text-align:center;color:var(--white);font-weight:600;font-size:16px}

/* products */
.card{position:absolute;top:1927px;width:303px;height:444px;background:var(--white);box-shadow:0 2px 10px rgba(0,0,0,.15)}
.card .photo{position:absolute;left:4px;top:4px;width:295px;height:257px}
.card .icon{position:absolute;right:14px;width:36px;height:36px;border-radius:50%;background:var(--white);display:flex;align-items:center;justify-content:center}
.card h3{position:absolute;top:280px;width:100%;text-align:center;font-size:17px;font-weight:600}
.card .stars{position:absolute;top:312px;width:100%;text-align:center;color:var(--star);font-size:14px;letter-spacing:1px}
.card .price{position:absolute;top:338px;width:100%;text-align:center;font-size:20px}
.card .price s{font-size:12px;text-decoration:none;font-weight:600;margin-right:6px}

/* why */
.why{position:absolute;left:0;top:2558px;width:1200px;height:611px;background:var(--blue);color:var(--white)}
.why h2{color:var(--white)}
.feat h4{font-size:18px;font-weight:500;color:#fff;margin-bottom:8px}
.feat p{font-size:13px;line-height:26px;color:#e8f3fa}
.feat{position:absolute;width:350px}
.feat.left{text-align:right}
.why-icon{position:absolute;width:72px;height:72px;border-radius:50%;background:var(--white);display:flex;align-items:center;justify-content:center}

/* blog */
.post{position:absolute;top:3367px;width:290px}
.post .photo{width:290px;height:284px;border-radius:10px}
.post h3{margin-top:28px;font-size:19px;font-weight:600;line-height:28px;padding:0 10px}
.post p{margin-top:12px;font-size:13px;line-height:26px;color:#444;padding:0 11px}
.post .date{margin-top:6px;padding:0 16px;font-size:14px;font-weight:600;display:flex;align-items:center;gap:10px}

/* newsletter */
.news{position:absolute;left:174px;top:3985px;width:850px;height:330px;background:var(--white);border-radius:18px;box-shadow:0 2px 12px rgba(0,0,0,.15)}
.news h2{position:absolute;top:50px;width:100%;text-align:center;font-size:36px;font-weight:600}
.news h2 span{color:var(--green)}
.news p{position:absolute;top:158px;width:100%;text-align:center;font-size:13px}
.news .field{position:absolute;left:160px;top:216px;width:530px;height:48px;border:2px solid #333;border-radius:26px;font-size:13px;padding:13px 20px}
.news .sub{position:absolute;left:528px;top:218px;width:160px;height:44px;background:var(--blue-btn);border-radius:22px;color:var(--white);font-weight:600;font-size:13px;display:flex;align-items:center;justify-content:center}

/* footer */
.footer-col{position:absolute;top:4372px;font-size:14px}
.footer-col h5{font-size:17px;font-weight:500;margin-bottom:18px}
.footer-col li{list-style:none;margin-bottom:14px;display:flex;align-items:center;gap:10px}
.contact-row{display:flex;gap:12px;align-items:flex-start;font-size:14px;line-height:24px;margin-bottom:22px;color:#333}
.ci{width:28px;height:28px;border-radius:50%;background:var(--green);flex:none;display:flex;align-items:center;justify-content:center}
</style>
</head>
<body>

<!-- HERO -->
<section class="hero">
  <div class="hero-photo" role="img" aria-label="Indoor hemp grow room with plants under purple grow lights"></div>
  <svg class="abs" style="left:0;top:500px" width="1200" height="145" viewBox="0 0 1200 145">
    <path d="M0 40 Q600 240 1200 40 L1200 145 L0 145Z" fill="#fff"/>
  </svg>
  <nav class="nav">
    <div style="position:absolute;left:27px;display:flex;align-items:center">
      <a class="active" href="#">HOME</a><span class="sep">|</span>
      <a href="#">ABOUT US</a><span class="sep">|</span>
      <a href="#">SHOP</a><span class="sep">|</span>
      <a href="#">LAB RESULTS</a>
    </div>
    <div style="position:absolute;left:567px;display:flex;align-items:center"><span class="sep">|</span><a href="#">CONTACT</a></div>
    <div class="search">Search
      <svg class="abs" style="right:4px;top:6px" width="16" height="16" viewBox="0 0 16 16"><circle cx="6.5" cy="6.5" r="5" fill="none" stroke="#222" stroke-width="1.5"/><line x1="10" y1="10" x2="15" y2="15" stroke="#222" stroke-width="1.5"/></svg>
    </div>
    <svg class="abs" style="left:862px;top:18px" width="24" height="22" viewBox="0 0 24 22"><path d="M12 20 C2 12 0 8 3 4 C6 0 10 2 12 5 C14 2 18 0 21 4 C24 8 22 12 12 20Z" fill="none" stroke="#222" stroke-width="2"/></svg>
    <svg class="abs" style="left:903px;top:14px" width="30" height="28" viewBox="0 0 30 28"><path d="M2 5 H7 L10 19 H23 L26 9 H8" fill="none" stroke="#222" stroke-width="2"/><circle cx="12" cy="23" r="2" fill="#222"/><circle cx="21" cy="23" r="2" fill="#222"/><circle cx="25" cy="4" r="4" fill="#e8c21a"/></svg>
  </nav>
  <div class="brand-badge">Ridgeline<br>Hemp</div>
  <h1><span class="accent">Premium Hemp,</span><br>Lab-Tested for Purity</h1>
  <p class="hero-sub">All products are third-party lab tested and sourced in the USA</p>
  <a class="btn btn-green" style="left:520px;top:412px;width:160px;height:42px">Shop Now</a>
</section>

<!-- ABOUT -->
<section class="about">
  <div class="about-img" style="left:132px;top:725px;width:216px;height:172px;background:linear-gradient(135deg,#2f4a26,#6b8a3e)" role="img" aria-label="Close-up of hemp flower buds"></div>
  <div class="about-img" style="left:362px;top:742px;width:214px;height:170px;background:linear-gradient(135deg,#1f2a18,#58702f)" role="img" aria-label="Vape pen resting on hemp buds"></div>
  <div class="about-img" style="left:132px;top:913px;width:216px;height:170px;background:linear-gradient(135deg,#8d7a6a,#c0565a)" role="img" aria-label="Hemp edibles gummies on a table"></div>
  <div class="about-img" style="left:362px;top:928px;width:214px;height:172px;background:linear-gradient(135deg,#2c3d1f,#b57a23)" role="img" aria-label="Dropper with hemp oil bottle"></div>
  <div class="abs" style="left:288px;top:845px;width:130px;height:130px;border-radius:50%;background:var(--green);border:5px solid #fff;display:flex;align-items:center;justify-content:center;color:#fff;font-size:15px;font-weight:600;text-align:center;line-height:18px">Ridgeline<br>Hemp</div>
  <h2>About <span>Us</span></h2>
  <div class="abs" style="left:637px;top:778px;width:56px;height:4px;background:var(--blue)"></div>
  <p>Lorem Ipsum is simply dummy text of the printing and typesetting industry. Lorem Ipsum has been the industry's standard dummy text ever since the 1500s, when an unknown printer took a galley of type and scrambled it to make a type specimen book. It has survived not only five centuries, but also the leap into electronic typesetting, remaining essentially unchanged. It was popularised in the 1960s with the release of Letraset sheets containing</p>
  <a class="btn btn-blue" style="left:634px;top:1053px;width:160px;height:42px">Read More</a>
</section>

<!-- CATEGORIES -->
<section>
  <svg class="abs" style="left:0;top:1233px" width="1200" height="350" viewBox="0 0 1200 350">
    <path d="M0 0 H1200 V345 Q600 230 0 345Z" fill="var(--green)"/>
  </svg>
  <h2 class="section-title" style="top:1315px;color:#fff;font-size:34px">Shop By Categories</h2>
  <div class="abs" style="left:572px;top:1390px;width:56px;height:4px;background:#fff"></div>
  <div class="cat-circle" style="left:120px;top:1474px;width:232px;height:232px;background:radial-gradient(circle,#8b6a3a,#3b3a22)" role="img" aria-label="THCA flower buds"><div class="cat-label">THCA Flower</div></div>
  <div class="cat-circle" style="left:612px;top:1474px;width:230px;height:230px;background:radial-gradient(circle,#7a8890,#2a2e2a)" role="img" aria-label="Vape pen on dark background"><div class="cat-label">Vapes</div></div>
  <div class="cat-circle" style="left:842px;top:1474px;width:236px;height:236px;background:radial-gradient(circle,#4f7a2e,#3c2e24)" role="img" aria-label="Hemp edibles with leaves"><div class="cat-label">Edibles</div></div>
  <div class="cat-circle" style="left:334px;top:1431px;width:292px;height:292px;background:radial-gradient(circle at 50% 40%,#9a6a22,#2d4a1f 70%)" role="img" aria-label="Concentrate oil bottle among hemp leaves"><div class="cat-label" style="bottom:26px">Concentrates</div></div>
</section>

<!-- FEATURED -->
<section>
  <h2 class="section-title" style="top:1808px">Featured <span>Products</span></h2>
  <div class="rule" style="top:1878px"></div>

  <div class="card" style="left:121px">
    <div class="photo" style="background:linear-gradient(135deg,#2e5a22,#1a1a1a 50%,#3f7a2e)" role="img" aria-label="Black product bottle among hemp leaves"></div>
    <div class="icon" style="top:22px"><svg width="20" height="18" viewBox="0 0 24 22"><path d="M12 20 C2 12 0 8 3 4 C6 0 10 2 12 5 C14 2 18 0 21 4 C24 8 22 12 12 20Z" fill="none" stroke="#222" stroke-width="2"/></svg></div>
    <div class="icon" style="top:74px"><svg width="18" height="18" viewBox="0 0 18 18"><rect x="2" y="5" width="14" height="12" rx="2" fill="none" stroke="#222" stroke-width="1.6"/><path d="M6 7 V4 a3 3 0 0 1 6 0 V7" fill="none" stroke="#222" stroke-width="1.6"/></svg></div>
    <h3>THCA Flower</h3><div class="stars">★★★★★</div>
    <div class="price"><s>$93.88</s>$54.49</div>
    <a class="btn btn-green" style="left:71px;top:388px;width:160px;height:42px">Shop Now</a>
  </div>
  <div class="card" style="left:450px">
    <div class="photo" style="background:radial-gradient(circle at 50% 65%,#e0a22a,#c9d1c4 45%,#4c7a3a)" role="img" aria-label="Jar of amber hemp concentrate with leaves"></div>
    <div class="icon" style="top:22px"><svg width="20" height="18" viewBox="0 0 24 22"><path d="M12 20 C2 12 0 8 3 4 C6 0 10 2 12 5 C14 2 18 0 21 4 C24 8 22 12 12 20Z" fill="none" stroke="#222" stroke-width="2"/></svg></div>
    <div class="icon" style="top:74px"><svg width="18" height="18" viewBox="0 0 18 18"><rect x="2" y="5" width="14" height="12" rx="2" fill="none" stroke="#222" stroke-width="1.6"/><path d="M6 7 V4 a3 3 0 0 1 6 0 V7" fill="none" stroke="#222" stroke-width="1.6"/></svg></div>
    <h3>Concentrates</h3><div class="stars">★★★★★</div>
    <div class="price"><s>$93.88</s>$54.49</div>
    <a class="btn btn-green" style="left:71px;top:388px;width:160px;height:42px">Shop Now</a>
  </div>
  <div class="card" style="left:778px">
    <div class="photo" style="background:linear-gradient(135deg,#1f3a1c,#3d6a30,#1c2e18)" role="img" aria-label="Vape pen lying on hemp leaves"></div>
    <div class="icon" style="top:22px"><svg width="20" height="18" viewBox="0 0 24 22"><path d="M12 20 C2 12 0 8 3 4 C6 0 10 2 12 5 C14 2 18 0 21 4 C24 8 22 12 12 20Z" fill="none" stroke="#222" stroke-width="2"/></svg></div>
    <div class="icon" style="top:74px"><svg width="18" height="18" viewBox="0 0 18 18"><rect x="2" y="5" width="14" height="12" rx="2" fill="none" stroke="#222" stroke-width="1.6"/><path d="M6 7 V4 a3 3 0 0 1 6 0 V7" fill="none" stroke="#222" stroke-width="1.6"/></svg></div>
    <h3>Vapes</h3><div class="stars">★★★★★</div>
    <div class="price"><s>$93.88</s>$54.49</div>
    <a class="btn btn-green" style="left:71px;top:388px;width:160px;height:42px">Shop Now</a>
  </div>
  <a class="btn btn-blue" style="left:519px;top:2429px;width:160px;height:42px">View More</a>
</section>

<!-- WHY CHOOSE US -->
<section class="why">
  <h2 class="section-title" style="top:70px;color:#fff">Why Choose Us</h2>
  <div class="abs" style="left:572px;top:145px;width:56px;height:4px;background:#fff"></div>
  <svg class="abs" style="left:400px;top:180px" width="400" height="360" viewBox="0 0 400 360">
    <circle cx="200" cy="177" r="178" fill="none" stroke="#fff" stroke-width="1.5" stroke-dasharray="6 6"/>
  </svg>
  <div class="abs" style="left:477px;top:234px;width:246px;height:246px;border-radius:50%;background:var(--green);border:8px solid #fff;display:flex;align-items:center;justify-content:center;color:#fff;font-size:26px;font-weight:600;text-align:center;line-height:32px">Ridgeline<br>Hemp</div>

  <div class="why-icon" style="left:426px;top:229px"><svg width="38" height="38" viewBox="0 0 38 38"><path d="M12 4 V16 L5 32 H21 L15 16 V4" fill="none" stroke="var(--blue)" stroke-width="2"/><rect x="24" y="10" width="8" height="22" rx="2" fill="none" stroke="var(--blue)" stroke-width="2"/></svg></div>
  <div class="why-icon" style="left:719px;top:229px"><svg width="38" height="38" viewBox="0 0 38 38"><circle cx="19" cy="15" r="10" fill="none" stroke="var(--blue)" stroke-width="2"/><path d="M13 24 L10 35 L19 31 L28 35 L25 24" fill="none" stroke="var(--blue)" stroke-width="2"/><path d="M19 10 L21 14 L25 14 L22 17 L23 21 L19 18 L15 21 L16 17 L13 14 L17 14Z" fill="var(--blue)"/></svg></div>
  <div class="why-icon" style="left:404px;top:406px"><svg width="40" height="30" viewBox="0 0 40 30"><rect x="2" y="3" width="36" height="24" fill="none" stroke="var(--blue)" stroke-width="2"/><rect x="2" y="3" width="14" height="11" fill="var(--blue)"/><line x1="16" y1="9" x2="38" y2="9" stroke="var(--blue)" stroke-width="2"/><line x1="2" y1="16" x2="38" y2="16" stroke="var(--blue)" stroke-width="2"/><line x1="2" y1="22" x2="38" y2="22" stroke="var(--blue)" stroke-width="2"/></svg></div>
  <div class="why-icon" style="left:724px;top:414px"><svg width="40" height="30" viewBox="0 0 40 30"><rect x="2" y="5" width="22" height="16" fill="none" stroke="var(--blue)" stroke-width="2"/><path d="M24 10 H32 L38 16 V21 H24" fill="none" stroke="var(--blue)" stroke-width="2"/><circle cx="10" cy="24" r="3" fill="#fff" stroke="var(--blue)" stroke-width="2"/><circle cx="31" cy="24" r="3" fill="#fff" stroke="var(--blue)" stroke-width="2"/></svg></div>

  <div class="feat left" style="left:49px;top:224px"><h4>Third-Party Lab Tested</h4><p>Every batch is independently tested to<br>guarantee purity and potency.</p></div>
  <div class="feat" style="left:818px;top:218px"><h4>Premium Quality</h4><p>Only the cleanest, most effective hemp<br>products make it to our shelves.</p></div>
  <div class="feat left" style="left:30px;top:408px;width:350px"><h4>Sourced in the USA</h4><p>All hemp is grown and harvested from trusted<br>American farms.</p></div>
  <div class="feat" style="left:815px;top:410px"><h4>Fast, Discreet Shipping</h4><p>Your order is delivered quickly and in<br>private, secure packaging.</p></div>
</section>

<!-- BLOG -->
<section>
  <h2 class="section-title" style="top:3250px">Our <span>Blog</span></h2>
  <div class="rule" style="top:3320px"></div>
  <article class="post" style="left:143px">
    <div class="photo" style="background:linear-gradient(160deg,#3e6a2e,#6b8ab0 60%,#2a3a5a)" role="img" aria-label="Gloved hand holding a hemp plant"></div>
    <h3>Lorem Ipsum is simply dummy</h3>
    <p>Lorem Ipsum is simply dummy text of the printing and typesetting industry.</p>
    <div class="date"><svg width="18" height="18" viewBox="0 0 18 18"><circle cx="9" cy="9" r="7.5" fill="none" stroke="#222" stroke-width="1.5"/><path d="M9 4 V9 L12 11" fill="none" stroke="#222" stroke-width="1.5"/></svg>Augest 9,2025</div>
  </article>
  <article class="post" style="left:451px">
    <div class="photo" style="background:linear-gradient(135deg,#1c2e18,#4a7a33,#1a2a16)" role="img" aria-label="Vape pen on hemp leaves"></div>
    <h3>Lorem Ipsum is simply dummy</h3>
    <p>Lorem Ipsum is simply dummy text of the printing and typesetting industry.</p>
    <div class="date"><svg width="18" height="18" viewBox="0 0 18 18"><circle cx="9" cy="9" r="7.5" fill="none" stroke="#222" stroke-width="1.5"/><path d="M9 4 V9 L12 11" fill="none" stroke="#222" stroke-width="1.5"/></svg>Augest 9,2025</div>
  </article>
  <article class="post" style="left:763px">
    <div class="photo" style="background:radial-gradient(circle at 55% 50%,#6f7a3a,#5a3a22 70%)" role="img" aria-label="Dried hemp bud on a wooden surface"></div>
    <h3>Lorem Ipsum is simply dummy</h3>
    <p>Lorem Ipsum is simply dummy text of the printing and typesetting industry.</p>
    <div class="date"><svg width="18" height="18" viewBox="0 0 18 18"><circle cx="9" cy="9" r="7.5" fill="none" stroke="#222" stroke-width="1.5"/><path d="M9 4 V9 L12 11" fill="none" stroke="#222" stroke-width="1.5"/></svg>Augest 9,2025</div>
  </article>
  <a class="btn btn-blue" style="left:519px;top:3862px;width:160px;height:42px">View More</a>
</section>

<!-- NEWSLETTER + FOOTER -->
<svg class="abs" style="left:0;top:4150px" width="1200" height="523" viewBox="0 0 1200 523">
  <path d="M0 80 Q600 -60 1200 80 V523 H0Z" fill="var(--pale)"/>
</svg>
<section class="news">
  <h2>Subscribe To Our <span>Newsletter</span></h2>
  <p>Be the first to know about new strains, exclusive deals, and lab-tested drops.</p>
  <div class="field">Enter Your Email Address</div>
  <div class="sub">SUBSCRIBE</div>
</section>

<footer>
  <div class="abs" style="left:160px;top:4375px;width:176px;height:176px;border-radius:50%;background:var(--green);border:6px solid #fff;display:flex;align-items:center;justify-content:center;color:#fff;font-size:20px;font-weight:600;text-align:center;line-height:26px">Ridgeline<br>Hemp</div>
  <div class="footer-col" style="left:424px">
    <h5>QUICK LINKS</h5>
    <ul><li>➜ Home</li><li>➜ About us</li><li>➜ Shop</li><li>➜ Lab Results</li></ul>
  </div>
  <div class="footer-col" style="left:633px">
    <h5>HELP LINKS</h5>
    <ul><li>➜ Contact Us</li><li>➜ Privacy Policy</li><li>➜ Support Links</li><li>➜ Terms and conditions</li></ul>
  </div>
  <div class="footer-col" style="left:872px">
    <h5>CONTACT US</h5>
    <div class="contact-row"><span class="ci"><svg width="12" height="14" viewBox="0 0 12 14"><path d="M6 13 C2 8 1 6 1 5 a5 5 0 0 1 10 0 c0 1 -1 3 -5 8Z" fill="#fff"/><circle cx="6" cy="5" r="2" fill="var(--green)"/></svg></span><span>Ridgeline Hemp<br>Newyork USA</span></div>
    <div class="contact-row"><span class="ci"><svg width="14" height="14" viewBox="0 0 14 14"><path d="M3 1 L5 1 L6 4 L4.5 5.5 C5.5 7.5 6.5 8.5 8.5 9.5 L10 8 L13 9 L13 11 C13 12 12 13 11 13 C5 13 1 9 1 3 C1 2 2 1 3 1Z" fill="#fff"/></svg></span><span>+1 555 010 0199</span></div>
    <div class="contact-row"><span class="ci"><svg width="14" height="10" viewBox="0 0 14 10"><rect x="0" y="0" width="14" height="10" rx="1" fill="#fff"/><path d="M0 0 L7 6 L14 0" fill="none" stroke="var(--green)" stroke-width="1.3"/></svg></span><span>info@ridgelinehemp.example</span></div>
  </div>
  <div class="abs" style="left:120px;top:4596px;width:960px;height:1px;background:#333"></div>
  <p class="abs" style="left:0;top:4618px;width:1200px;text-align:center;font-size:13px">Copyrights 2025. Ridgeline Hemp .All Rights Reserved</p>
</footer>

</body>
</html>
```